High Quality fast food restaurant - Tomanyo

Tomanyo is a fast food company with its target's focused on logistic, simplicity, high quality, freshness and modern.

We need a web design where the customers can get a complete idea of our high quality completeness, we want to take fast food to a new upper level.

We would like to see the colours of wood and metal. Pictures have been attached of our local.

We would like to have something in similar to: http://www.qpz.example/
Updates

Images for the food we are going to sell can be found here: http://shrt.example/uWQa7

It will be the images with rice, french fries or pita bread.

Target Market(s)

The fast food eating people between sloppy food and restaurant level.

Industry/Entity Type

Fast Food Restaurant

Requirements
Should not have
• No Flash or Java

```html
<!DOCTYPE html>
<html lang="en">
<head>
<meta charset="utf-8">
<title>Tomanyo – Fast Food</title>
<link href="https://fonts.googleapis.com/css2?family=Cabin:wght@400;600;700&family=Marcellus&family=Italianno&family=Titan+One&display=swap" rel="stylesheet">
<style>
:root{
  --wood:#8f6c49;
  --brown-dark:#3d0b04;
  --brown:#5a1408;
  --cream:#f6e3c8;
  --nav-bg:#f3dcc0;
  --nav-text:#3a1a0c;
  --orange:#f5a10c;
  --page:#ececec;
  --white:#ffffff;
  --text:#333333;
  --chirp:#3bb9e8;
  --friend:#3a5a9b;
  --red:#b0101a;
}
*{margin:0;padding:0;box-sizing:border-box}
html,body{width:1200px;height:1106px;overflow:hidden}
body{background:linear-gradient(#fff,var(--page));font-family:"Cabin",sans-serif;color:var(--text);position:relative}
.wood-strip{position:absolute;left:0;width:1200px;background:var(--wood)}
.header{position:absolute;top:17px;left:0;width:1200px;height:150px;background:radial-gradient(ellipse at 30% 40%,#5e1c0c,var(--brown-dark) 70%)}
.logo{position:absolute;left:160px;top:24px;font-family:"Cabin",sans-serif;font-weight:700;font-size:62px;color:var(--cream);letter-spacing:1px;line-height:1}
.social-top{position:absolute;top:32px;width:44px;height:44px;border-radius:50%;background:var(--orange)}
.nav{position:absolute;left:144px;top:120px;width:918px;height:47px;background:linear-gradient(#fbeedd,var(--nav-bg));border-radius:4px 4px 0 0;display:flex;align-items:center}
.nav a{font-weight:600;font-size:16px;color:var(--nav-text);text-decoration:none;padding:0 14px;height:47px;line-height:47px;border-right:1px solid #d6b995;letter-spacing:.3px}
.nav a:first-child{padding-left:20px}
.nav .locations{position:absolute;right:8px;top:6px;height:34px;line-height:34px;background:var(--brown);color:var(--cream);border:none;border-radius:4px;padding:0 12px}
.hero{position:absolute;top:176px;left:0;width:1200px;height:580px;overflow:hidden;background:linear-gradient(110deg,#a8713c 0%,#8a5528 55%,#5a1a0a 80%,#4a0e06 100%)}
.headline{position:absolute;left:150px;top:28px;font-family:"Marcellus",serif;font-weight:400;font-size:80px;line-height:76px;color:#fff}
.food{position:absolute;border-radius:40px}
.pager{position:absolute;left:150px;top:540px;width:67px;height:20px;border-radius:10px;background:#f1f1f1;display:flex;gap:4px;justify-content:center;align-items:center}
.pager i{width:7px;height:7px;border-radius:50%;background:#c0131a}
.pager i:first-child{background:#333}
.card{position:absolute;top:794px;width:287px;height:176px;border-radius:6px;overflow:hidden;text-decoration:none}
.card .plus{position:absolute;left:0;bottom:0;width:20px;height:20px;background:var(--orange);color:var(--brown-dark);font-weight:700;font-size:15px;line-height:20px;text-align:center}
.card-butter{left:142px;background:linear-gradient(120deg,#e9842a,#c8530c)}
.card-butter .title{position:absolute;left:22px;top:44px;font-family:"Italianno",cursive;font-size:48px;line-height:38px;color:#fff}
.card-stack{left:458px;background:linear-gradient(120deg,#5e3d28,#3a2215)}
.card-stack .title{position:absolute;left:18px;top:22px;font-family:"Titan One",sans-serif;color:var(--orange);font-size:22px;line-height:26px}
.card-stack .title em{font-family:"Italianno",cursive;font-style:normal;font-size:42px;display:block;line-height:34px}
.card-offers{left:775px;background:linear-gradient(#b8d46a,#8fb43a)}
.card-offers .title{position:absolute;left:10px;top:40px;font-family:"Titan One",sans-serif;font-size:24px;line-height:28px;color:#1a1a0a}
.card-offers .price{position:absolute;right:0;top:0;background:var(--brown);color:#fff;font-family:"Titan One",sans-serif;font-size:24px;padding:2px 8px}
.share-bar{position:absolute;left:142px;top:994px;width:920px;height:57px;background:var(--white);border-radius:6px;display:flex;align-items:center}
.share-label{font-size:13px;letter-spacing:.4px;margin-left:14px;width:148px}
.share-btn{height:46px;width:201px;margin-right:8px;border-radius:3px;display:flex;align-items:center;color:#fff;font-size:10px;padding-left:6px}
.share-btn .sq{width:34px;height:34px;border-radius:3px;background:rgba(255,255,255,.35);margin-right:10px}
.share-btn .mini{display:flex;gap:3px;margin-top:4px;font-size:11px}
.share-btn .mini span{background:#fff;color:#333;padding:1px 5px;border-radius:2px}
.chirp{background:var(--chirp)}
.friend{background:var(--friend)}
.connect{margin-left:auto;margin-right:24px;display:flex;align-items:center;gap:4px;font-size:13px;letter-spacing:.4px}
.connect b{width:14px;height:14px;border-radius:2px;display:inline-block}
.footer{position:absolute;left:0;top:1058px;width:1200px;height:48px;background:linear-gradient(#fdfdfd,#e0e0e0);border-top:1px solid #ddd;font-size:13.5px}
.copy{position:absolute;left:140px;top:18px}
.connect-with{position:absolute;left:690px;top:20px;letter-spacing:.4px;font-size:12.5px}
.newsletter{position:absolute;left:814px;top:15px;width:188px;height:24px;background:#fff;border:1px solid #ccc;font-size:12px;padding:4px 6px;color:#333}
.submit{position:absolute;left:1002px;top:15px;width:60px;height:24px;background:var(--red);color:#fff;font-size:12.5px;text-align:center;line-height:24px}
</style>
</head>
<body>
<div class="wood-strip" style="top:0;height:17px"></div>
<header class="header">
  <div class="logo">TOMANYO</div>
  <span class="social-top" style="left:967px" aria-label="Friendbook"></span>
  <span class="social-top" style="left:1021px" aria-label="Chirpline"></span>
</header>
<nav class="nav">
  <a href="#">HOME</a><a href="#">MENU</a><a href="#">FRESH OFFERS</a><a href="#">DELIVERS</a><a href="#">COMPANY INFORMATION</a><a href="#">CONTACT US</a>
  <a class="locations" href="#">LOCATIONS</a>
</nav>
<div class="wood-strip" style="top:167px;height:9px"></div>
<section class="hero" role="img" aria-label="Blurred restaurant backdrop with decorative ribbons">
  <h1 class="headline">Delicious Starts<br>Right Here.</h1>
  <div class="food" role="img" aria-label="Photo of a crunchy beef taco" style="left:240px;top:200px;width:360px;height:290px;background:linear-gradient(#dcb448,#c4962e)"></div>
  <div class="food" role="img" aria-label="Photo of a double cheeseburger with lettuce and tomato" style="left:615px;top:135px;width:445px;height:370px;background:linear-gradient(#d8a05a,#b86a3a 60%,#d8a05a)"></div>
  <div class="pager"><i></i><i></i><i></i><i></i></div>
</section>
<div class="wood-strip" style="top:756px;height:10px"></div>

<a class="card card-butter" href="#" role="img" aria-label="Photo of a bacon and egg breakfast burger">
  <div class="title">Butter<br>Burger</div><span class="plus">+</span>
</a>
<a class="card card-stack" href="#" role="img" aria-label="Photo of a three cheese burger">
  <div class="title"><em>New</em>THREE<br>CHEESE<br>STACKBURGER</div><span class="plus">+</span>
</a>
<a class="card card-offers" href="#" role="img" aria-label="Photo of a burger with a cold drink">
  <div class="title">View all<br>Offers<br>and<br>Promotions</div><div class="price">$1.29</div><span class="plus">+</span>
</a>

<div class="share-bar">
  <span class="share-label">SHARE WITH A FRIEND</span>
  <div class="share-btn chirp"><span class="sq"></span><div>LIKE US ON CHIRPLINE!<div class="mini"><span>Chirp</span><span>0</span></div></div></div>
  <div class="share-btn friend"><span class="sq"></span><div>LIKE US ON FRIENDBOOK!<div class="mini"><span>Like</span><span>12</span></div></div></div>
  <div class="connect">CONNECT TO US&nbsp;&nbsp;<b style="background:#3a5a9b"></b><b style="background:#3bb9e8"></b><b style="background:#c4302b"></b><b style="background:#1f78b4"></b></div>
</div>

<footer class="footer">
  <span class="copy">© 2013 Tomanyo. All Rights Reserved.</span>
  <span class="connect-with">CONNECT WITH US</span>
  <span class="newsletter">Subscribe to newsletter...</span>
  <span class="submit">Submit</span>
</footer>
</body>
</html>
```